Web Site Design for new Children's Book Series

We need a new web site design that complements a new children's book series that will be available next month. The main character is named 'Mippo Zelka Otter Cat Finch' and the story lines work through bullying issues for elementary age kids. This is a new design from scratch, but we have attached a collection of artwork from the new book series that the web site design should complement.

The scope of this project is only for the design / layout of the home page and one interior page for the web site.

Additional project details including the sitemap and example content are included in the attached document: 'Mippo Zelka Web Site.pdf'

We are open for questions and we look forward to seeing your creativity!
Updates

We have marked the project as guaranteed now!  We look forward to seeing your ideas and concepts!

Target Market(s)

Currently, there are two children’s books in the Mippo Zelka series aimed at elementary aged children. This collection is planned to grow over time. The goal of the web site is to provide information about the authors and the book series to elementary aged children (ages 3 to 12), their parents, and their school teachers and counselors.

Industry/Entity Type

Interior

Requirements
Must have
• The web site design should complement the attached artwork from the Mippo Zelka series. Overall, a full width design is desired that utilizes and open layout with lots of color.

The Mippo Zelka animal logo should be prominently placed. It is not necessary to retain the white background behind the logo.

The web site will be implemented as a responsive design using the Quill Scaffold framework and a standard 12 column grid.
Nice to have
• There are two themes in the books which should be incorporated into the web site design:

- Mippo Zelka uses the phrase “Way Cool” in describing various characters in the book and it is meant to build confidence and self esteem ... "you are way cool"

- An eagle feather is left behind as in “Zelka was here”. This eagle feature should be incorporated into the design in various locations.

```html
<!DOCTYPE html>
<html lang="en">
<head>
<meta charset="utf-8">
<title>Mippo Zelka – Home</title>
<link rel="stylesheet" href="https://fonts.googleapis.com/css2?family=Neucha&display=swap">
<style>
:root{
  --sky-top:#3aa2cf;
  --sky-bottom:#63d9ef;
  --ink:#1d1d1d;
  --white:#ffffff;
  --purple:#8370b8;
  --sage:#86baa5;
  --rose:#c06167;
  --olive:#b9b985;
  --periwinkle:#7596d0;
  --footer:#66dff0;
  --feather-tone:rgba(20,20,20,.6);
  --art-green:#7fb356;
  --art-water:#58b9de;
  --art-brown:#8a5a2e;
}
*{box-sizing:border-box;margin:0;padding:0}
html,body{width:808px;height:1200px;overflow:hidden;background:var(--white)}
body{position:relative;font-family:"Neucha",cursive;color:var(--ink)}
h2{font-weight:normal}
.sky{position:absolute;left:0;top:0;width:808px;height:320px;background:linear-gradient(var(--sky-top),var(--sky-bottom))}
.clouds{position:absolute;left:0;top:240px;width:808px;height:100px}
.main-nav{position:absolute;top:22px;left:66px;width:676px;display:flex;justify-content:space-between;font-size:17px;line-height:22px}
.main-nav a{color:var(--ink);text-decoration:none;white-space:nowrap}
.story-card{position:absolute;width:136px;height:172px;border:7px solid var(--white);border-radius:14px}
.circle{position:absolute;width:253px;height:253px;border-radius:50%}
.circle-text{position:absolute;font-size:10px;line-height:14.3px;white-space:nowrap}
.circle-title{font-size:14.5px;line-height:17px}
.centered{text-align:center}
.feather-art{position:absolute;width:84px;height:60px;border-radius:50%;background:radial-gradient(ellipse at center,var(--feather-tone),rgba(20,20,20,0) 70%)}
.art{position:absolute}
.link-light{color:var(--white);text-decoration:none}
.news-band{position:absolute;left:0;top:633px;width:808px;height:170px;background:var(--rose)}
.blog-list{position:absolute;left:65px;top:22px;font-size:12.5px;line-height:17.5px;list-style:none;white-space:nowrap}
.blog-title{font-size:15.5px;line-height:20px}
.signup{position:absolute;right:68px;top:22px;width:300px;text-align:right}
.signup h2{font-size:15.5px;line-height:20px;margin-bottom:5px;white-space:nowrap}
.signup input{display:block;width:206px;height:22px;margin:0 0 8px auto;border:0;padding:0 7px;font:12px "Neucha",cursive;color:var(--ink)}
.signup input::placeholder{color:var(--ink)}
.signup button{width:102px;height:22px;border:0;background:var(--white);font:12px "Neucha",cursive;color:var(--ink)}
.chat-icon{position:absolute}
.readers-text{position:absolute;left:470px;top:932px;width:230px;font-size:8px;line-height:12.3px}
.readers-text .by{text-align:right}
.site-footer{position:absolute;left:0;top:1149px;width:808px;height:51px;background:var(--footer);text-align:center;line-height:51px;font-size:15.5px}
</style>
</head>
<body>
<div class="sky"></div>

<nav class="main-nav">
  <a href="#">Home</a><a href="#">About the Authors</a><a href="#">The Books</a><a href="#">Schedule a Visit</a><a href="#">Glow and Grow</a><a href="#">Teachable Moments</a><a href="#">Contact Us</a><a href="#">Blog</a>
</nav>

<div class="story-card" role="img" aria-label="Story scene: the hound dog asleep by his red doghouse in the woods" style="left:78px;top:66px;transform:rotate(-3deg);background:linear-gradient(#3f7a3a,var(--art-green))"></div>
<div class="story-card" role="img" aria-label="Story scene: the eagle and an owl perched on a branch" style="left:250px;top:66px;transform:rotate(2deg);background:linear-gradient(#5f9c45,var(--art-green))"></div>
<div class="story-card" role="img" aria-label="Story scene: the eagle resting on a riverbank" style="left:422px;top:70px;transform:rotate(-2deg);background:linear-gradient(#6b7d3a 35%,var(--art-water))"></div>
<div class="story-card" role="img" aria-label="Story scene: the eagle flying over the river at sunset" style="left:603px;top:66px;transform:rotate(3deg);background:linear-gradient(#f0b27a,#7fc7a0 40%,var(--art-water))"></div>

<svg class="clouds" viewBox="0 0 808 100" aria-hidden="true">
  <path fill="#ffffff" d="M0 70 Q40 40 90 55 Q130 20 190 45 Q240 10 300 40 Q350 25 390 50 Q440 15 500 35 Q540 5 600 30 Q650 15 690 40 Q740 20 808 35 L808 100 L0 100Z"/>
</svg>

<!-- Introducing -->
<div class="circle" style="left:102px;top:342px;background:var(--purple)"></div>
<div class="art" role="img" aria-label="Character art: the hound dog with the eagle perched behind him" style="left:76px;top:286px;width:113px;height:148px;border-radius:40% 40% 20% 20%;background:linear-gradient(135deg,#2a2a2a,var(--art-brown))"></div>
<div class="circle-text" style="left:187px;top:373px">
  <h2 class="circle-title">Introducing Mippo Zelka</h2>
  Mippo, the hound dog and Zelka, the<br>
  eagle, lived along the Willowmere River in<br>
  Alder Bend, North Carolina.
</div>
<div class="circle-text centered" style="left:106px;top:434px;width:248px">
  While playing one day, they became an<br>
  unusual character named Mippo Zelka Otter Cat Finch.<br>
  Mippo and Zelka travel throughout the book adjusting<br>
  to their new body and learning how to use their "super powers"<br>
  for good. They help kids learn how to feel good about<br>
  themselves, deal with bullying, and forgiveness.<br>
  A must read for young children.
</div>
<div class="feather-art" role="img" aria-label="Eagle feather illustration" style="left:230px;top:520px"></div>

<!-- New release -->
<div class="circle" style="left:456px;top:343px;background:var(--sage)"></div>
<div class="art" role="img" aria-label="Book cover: the hound dog and eagle on a dock with the series title" style="left:611px;top:286px;width:129px;height:170px;background:linear-gradient(#c84a3a,#d99a7a 35%,#5aa7b8)"></div>
<div class="circle-text centered" style="left:458px;top:375px;width:152px">
  <h2 class="circle-title">New Release</h2>
  When the dust finally settled, Mippo<br>
  and Zelka were lying on the ground,<br>
  knocked out. But wait -- there was<br>
  something very different about them.<br>
  The two of them were in one body!
</div>
<div class="circle-text centered" style="left:456px;top:463px;width:253px">
  The front legs were Mippo's, and the rear legs were Zelka's.<br>
  It was a hound dog body with fur, feathers and large wings.<br>
  There were two heads on the one body. One was Mippo's with<br>
  his floppy, hound dog-ears and hound dog nose; the other was<br>
  Zelka's with his white eagle feathers and<br>
  yellow beak.
</div>
<div class="feather-art" role="img" aria-label="Eagle feather illustration" style="left:577px;top:520px"></div>

<section class="news-band">
  <ul class="blog-list">
    <li class="blog-title">Blog Posts</li>
    <li>Have you heared the news abou... <a class="link-light" href="#">read more</a></li>
    <li>The hound dog bird is on the move... <a class="link-light" href="#">read more</a></li>
    <li>...and he said - Way Cool !... <a class="link-light" href="#">read more</a></li>
    <li>- I thought I heared something Zelka... <a class="link-light" href="#">read more</a></li>
    <li>We are going in circles you know <a class="link-light" href="#">read more</a></li>
    <li>That's more like it!... <a class="link-light" href="#">read more</a></li>
  </ul>
  <form class="signup">
    <h2>Get updates and news from Mippo and Zelka</h2>
    <input type="text" placeholder="Your name...">
    <input type="email" placeholder="Your email...">
    <button type="button">Keep me updated!</button>
  </form>
</section>

<!-- Author visits -->
<div class="circle" style="left:102px;top:849px;background:var(--olive)"></div>
<div class="art" role="img" aria-label="Photo of the two authors" style="left:186px;top:856px;width:88px;height:113px;background:linear-gradient(#3a3a3a,#1a1a1a)"></div>
<div class="circle-text centered" style="left:102px;top:973px;width:253px;font-size:12.5px;line-height:17.5px">
  <h2 class="circle-title" style="font-size:16px;line-height:19px">Author visits</h2>
  Would you like Theo and Marla to bring<br>
  Mippo and Zelka to your school?<br>
  Learn more <a class="link-light" href="#">here...</a>
</div>
<div class="feather-art" role="img" aria-label="Eagle feather illustration" style="left:230px;top:1026px"></div>

<!-- Readers -->
<div class="circle" style="left:456px;top:849px;background:var(--periwinkle)"></div>
<svg class="chat-icon" viewBox="0 0 44 40" style="left:593px;top:861px;width:42px;height:39px" aria-hidden="true">
  <path d="M4 3h36v24H22l-9 9v-9H4z" fill="#7596d0" stroke="#fff" stroke-width="3" stroke-linejoin="round"/>
  <path d="M22 23c-6-4-9-7-9-10a4 4 0 0 1 9-2 4 4 0 0 1 9 2c0 3-3 6-9 10z" fill="#fff"/>
</svg>
<svg class="chat-icon" viewBox="0 0 44 40" style="left:656px;top:877px;width:31px;height:30px" aria-hidden="true">
  <path d="M4 3h36v24H22l-9 9v-9H4z" fill="#7596d0" stroke="#fff" stroke-width="3" stroke-linejoin="round"/>
  <path d="M22 23c-6-4-9-7-9-10a4 4 0 0 1 9-2 4 4 0 0 1 9 2c0 3-3 6-9 10z" fill="#fff"/>
</svg>
<svg class="chat-icon" viewBox="0 0 44 40" style="left:696px;top:845px;width:44px;height:42px" aria-hidden="true">
  <path d="M4 3h36v24H31v9l-9-9H4z" fill="#7596d0" stroke="#fff" stroke-width="3" stroke-linejoin="round"/>
  <path d="M22 23c-6-4-9-7-9-10a4 4 0 0 1 9-2 4 4 0 0 1 9 2c0 3-3 6-9 10z" fill="#fff"/>
</svg>
<h2 class="circle-title" style="position:absolute;left:456px;top:903px;width:253px;text-align:center;font-size:16px;line-height:19px">From out Readers</h2>
<div class="readers-text">
  Lorem Ipsum is simply dummy text of the printing and typesetting industry. Lorem Ipsum has been the industry's standard dummy text ever since when an unknown printer took a book.
  <div class="by">- Amanda</div>
  <div style="margin-top:4px">Lorem Ipsum is simply dummy text of the printing and typesetting industry. Lorem Ipsum has been the industry's standard dummy text ever since when an unknown printer took a book.</div>
  <div class="by">- Oliver</div>
</div>
<div class="feather-art" role="img" aria-label="Eagle feather illustration" style="left:584px;top:1026px"></div>

<footer class="site-footer">Copyright © 2014, Mippo Zelka Enterprises</footer>
</body>
</html>
```